Web Re-Design for African Art Gallery

Introduction
We are an art gallery carrying artworks by contemporary African artists. We require a new, more modern website for our gallery.
The website idea. The key words we’d like to use to describe our website are - elegant, simple, uncluttered, easy to navigate, classy, interesting.
We’d like a website that is as uncluttered as possible; a simple, elegant website that lets viewers carry out the business of viewing our artworks online as easily as possible. A web site that is adventurous and arty without being complicated.
Our logo is a monochrome dark grey colour but this should not affect the colour scheme of the website. We are also open to a new logo if it is decidedly better than what we have at present, and would be willing to pay additionally for it if we take it.
Our audience is international. Art collectors worldwide looking for contemporary art. We do not want any African themed design.
Sections
The home page will have various sections – Artists, New Works, Publication, Mailing list, Exhibitions
Below are a list of gallery websites we like.
http://www.tarvelqonsik.example/
http://www.pembrowgallery.example/
http://www.dalefrunkwater.example/
http://www.quillopraxa.example/exhibitions/2011-12-13_velvet-arcades/
http://www.zot.vrbn.example/index.html
Requirement
We'd like a a home page template as well as a template for the sections in HTML.
We do not have a regular coder so we'd be happy to have the winning designer carry on with fitting the rest of the site to the template if the price is right.
Our present website is www.moonfernstudio.example. feel free to get logo, artwork pictures and any other material you might need from there.
Thanks

```html
<!DOCTYPE html>
<html lang="en">
<head>
<meta charset="utf-8">
<title>The Moonfern Gallery — Artists</title>
<link rel="stylesheet" href="https://fonts.googleapis.com/css2?family=Questrial&family=Noto+Serif:ital@1&display=swap">
<style>
  :root {
    --page-bg: #ffffff;
    --ink: #111111;
    --nav-muted: #8a8a8a;
    --body-muted: #8c8c8c;
    --rule: #e2e2e2;
    --footer-text: #8f8f8f;
    --logo-ink: #2b2b2b;
    --art-red: #b5203a;
    --art-red-deep: #9e1326;
  }
  * { margin: 0; padding: 0; box-sizing: border-box; }
  html, body {
    width: 1200px; height: 690px; overflow: hidden;
    background: var(--page-bg);
  }
  .site {
    position: relative; width: 1200px; height: 690px;
    font-family: "Questrial", "Helvetica Neue", Arial, sans-serif;
    color: var(--ink);
  }
  .header-rule {
    position: absolute; top: 121px; height: 1px; background: var(--rule);
  }
  .header-rule.left { left: 184px; width: 316px; }
  .header-rule.right { left: 680px; width: 304px; }
  .brand {
    position: absolute; left: 500px; top: 62px; width: 180px; height: 70px;
    display: flex; align-items: center; justify-content: center;
    font-size: 21px; color: var(--logo-ink); letter-spacing: 0.3px;
    text-decoration: none;
  }
  .main-nav {
    position: absolute; top: 160px; left: 0; width: 1170px;
    display: flex; justify-content: center; gap: 36px;
    list-style: none; font-size: 14.5px;
  }
  .main-nav a { color: var(--nav-muted); text-decoration: none; }
  .main-nav a.is-current { color: var(--ink); }
  .work-details {
    position: absolute; left: 184px; top: 239px; width: 330px;
  }
  .work-title { font-size: 15px; font-weight: normal; line-height: 18px; }
  .work-description {
    margin-top: 15px;
    font-family: "Noto Serif", Georgia, serif; font-style: italic;
    font-size: 12px; line-height: 18px; color: var(--body-muted);
  }
  .work-description + .work-description { margin-top: 18px; }
  .artwork {
    position: absolute; left: 550px; top: 241px; width: 431px; height: 285px;
    background: radial-gradient(ellipse at 45% 55%, var(--art-red) 0%, var(--art-red-deep) 100%);
    box-shadow: 0 1px 4px rgba(0,0,0,0.45);
  }
  .footer-rule {
    position: absolute; left: 184px; top: 583px; width: 800px; height: 1px;
    background: var(--rule);
  }
  .copyright {
    position: absolute; top: 605px; left: 0; width: 1168px;
    text-align: center; font-size: 12px; color: var(--footer-text);
  }
</style>
</head>
<body>
<div class="site">
  <header>
    <div class="header-rule left"></div>
    <a class="brand" href="#">The Moonfern Gallery</a>
    <div class="header-rule right"></div>
    <nav>
      <ul class="main-nav">
        <li><a class="is-current" href="#">Artists</a></li>
        <li><a href="#">New Works</a></li>
        <li><a href="#">Publications</a></li>
        <li><a href="#">Profiles</a></li>
        <li><a href="#">Exhibitions</a></li>
        <li><a href="#">Contact</a></li>
      </ul>
    </nav>
  </header>

  <main>
    <section class="work-details">
      <h1 class="work-title">Image Title</h1>
      <p class="work-description">Lorem ipsum dolor sit amet, consectetur adipiscing elit.<br>Nunc ultrices, lorem in fermentum laoreet</p>
      <p class="work-description">Sed nisl elit, eleifend in posuere et, ornare in eros.</p>
    </section>
    <div class="artwork" role="img" aria-label="Painting of a seated figure with a patterned body in red, yellow and brown tones against a deep red background"></div>
  </main>

  <footer>
    <div class="footer-rule"></div>
    <p class="copyright">Copyright © The Moonfern Gallery Limited. All rights reserved.</p>
  </footer>
</div>
</body>
</html>
```